Educational Brochure or Pamphlet Series

We are a nonprofit organization looking at revamping our template designs for our educational pamphlet series, as we edit and republish our content library for 2014. Most of the current content spans over 3 to 4 panel double-sided folded brochures, although we are not limited to that format moving forward. We would be looking for a design that is inviting prompting interest at initial pick up, while also being laid out in a manner where complex tips and advice is able to be digested by readers. We do not have a consistent brand currently among our materials so we are able to branch to a new more modern and professional look/theme, but at the same time i wouldn't want to to go so far away from our look that we clash with our colors/logo/identity.

I almost chose magazine as project type, because ideally i would prefer a design that has the ability to grow beyond a 3 panel foldable brochure, into a small multipage booklet or magazine bound style.

We are a nonprofit in the health advocacy realm that helps patients understand the insurance and medical industry so they can get and afford the care they need while battling a major illness. We have not updated our publication design in over 10 years and need a professional refresh. More about us can be found at www.carewaykinfolk.org
Updates

Thanks to everyone that has already contributed designs or those who have accepted the project invite and are still working on submission.    I appreciate your willingness to assist our organization and participate in the process.   I look forward to reviewing the designs soon.

I am excited to participate in my first project on Pixel Harbor, and look forward to working again on future projects within this platform.

If you have any questions or could benefit from additional explanation on aspects of the project, please feel free to reach out to me and I'd be happy to share any insight I have.

Marta

Target Market(s)

Our pamphlets and brochures are geared towards patients who have been diagnosed with serious illness (ex. cancer, ALS, MS) and who are navigating the healthcare system to get the care and medications they need. Patients or caregivers would pick up these brochures in cancer facilities, doctors office or through online research.

Included in uploaded files are a few of these current pamphlets, some of our more recently designed ads or promo pieces to see what we have been doing lately. If needed and requested, i'd be happy to provide links of some of the brochures of our favorite partners who have done a nice job with presenting similar information.

Industry/Entity Type

Insurance

Font styles to use
Sans Serif

Colors

Designer to choose colors to be used in the design.

Requirements
Must have
• -Information easy to read and digest
-professional and educational in focus
-a design that can be reasonably customized or modified to include a number of corollary topics in a similar structure to complete a full library.
-colorful (can be 2 color or 4 color print)
-enough white space to be pleasing to the eye and not overwhelming with text
Nice to have
• could work on a lighthouse or beacon of light theme. (possible, ok if not)
Should not have
• ideally no extreme die cuts or printing specs that would be exceptionally expensive to produce, given nonprofit budget

```html
<!DOCTYPE html>
<html lang="en">
<head>
<meta charset="utf-8">
<title>A Clearer Path — Second Opinions Brochure</title>
<link href="https://fonts.googleapis.com/css2?family=Source+Sans+3:wght@400;600;700&display=swap" rel="stylesheet">
<style>
:root{
  --blue:#1b7cc6;
  --blue-dark:#14609e;
  --blue-tint:#cfe4f5;
  --orange:#e9a21f;
  --ink:#4a4a4a;
  --paper:#ffffff;
  --stage:#e7e5e2;
  --photo-light:#d9d9d9;
  --photo-dark:#7c7c7c;
}
*{box-sizing:border-box;margin:0;padding:0}
html,body{width:1200px;height:1000px;overflow:hidden}
body{background:var(--stage);font-family:"Source Sans 3",Arial,sans-serif;color:var(--ink);position:relative}
.spread{position:absolute;left:40px;width:1120px;height:320px;display:flex;box-shadow:0 2px 10px rgba(0,0,0,.18)}
.spread--cost{top:22px}
.spread--intro{top:358px}
.page{position:relative;width:560px;height:320px;background:var(--paper);overflow:hidden}
.page + .page{border-left:1px solid #e4e4e4}
.shape{position:absolute;inset:0;width:100%;height:100%}
.photo{position:absolute;background:linear-gradient(135deg,var(--photo-light),var(--photo-dark))}
.cols{position:absolute;display:flex;gap:10px}
.col{width:110px;font-size:7.4px;line-height:9.4px}
.col p + p{margin-top:4px}
.col-head{color:var(--orange);font-weight:700;font-size:8.6px;line-height:10px;margin-bottom:3px}
.quote{position:absolute;font-weight:700;text-transform:uppercase;font-size:11px;line-height:13.5px}
.quote--white{color:#fff}
.quote--blue{color:var(--blue)}
.on-blue .col{color:var(--blue-tint)}
.title-big{position:absolute;color:#fff;font-weight:700;font-size:22px;line-height:23px}
.mission{position:absolute;color:#fff;font-size:7.6px;line-height:9.6px}
.mission h3{color:var(--orange);font-size:8.6px;line-height:10.5px}
.cover{position:absolute;top:690px;width:540px;height:290px;background:var(--paper);overflow:hidden;box-shadow:0 2px 10px rgba(0,0,0,.18)}
.cover--front{left:40px}
.cover--back{left:620px}
.brand{position:absolute;right:24px;top:138px;display:flex;align-items:center;gap:6px;color:var(--blue);font-weight:700;font-size:12px}
.brand-dot{width:10px;height:10px;background:var(--orange)}
.series{position:absolute;right:24px;top:176px;font-weight:600;font-size:10px;letter-spacing:.4px;color:#555}
.cover-title{position:absolute;right:24px;top:192px;text-align:right;color:var(--blue);font-weight:700;font-size:17px;line-height:20px}
.back-intro{position:absolute;left:40px;top:26px;width:460px;font-size:8px;line-height:10.5px}
.pubs{position:absolute;left:40px;top:82px;display:flex;gap:30px}
.pubs ul{list-style:none;width:200px}
.pubs li{font-size:8px;line-height:10px;margin-bottom:6px;padding-left:9px;position:relative;font-weight:600;color:#333}
.pubs li::before{content:"";position:absolute;left:0;top:3px;border-left:4px solid var(--blue);border-top:2.5px solid transparent;border-bottom:2.5px solid transparent}
.pubs li span{display:block;font-weight:400;color:#777;font-size:7px}
.contact{position:absolute;left:110px;bottom:24px;display:flex;gap:40px;font-size:8px;line-height:11px}
.contact .hl{color:var(--blue);font-weight:700}
</style>
</head>
<body>

<!-- Inside spread: physician choice and costs -->
<section class="spread spread--cost">
  <div class="page">
    <div class="cols" style="left:30px;top:80px">
      <div class="col">
        <h4 class="col-head">Choosing a Physician</h4>
        <p>There are many professional doctors in practice today. Family physicians provide comprehensive medical care with an emphasis on caring for all members of the family. A general surgeon is able to perform all types of surgical procedures aimed at treating a range of diseases and conditions, including cancer. Medical oncologists are specialists that use various medications to treat and manage patients with cancer. This may include the use of chemotherapy to kill cancer cells, painkillers and other drugs.</p>
      </div>
      <div class="col">
        <p>Radiation oncologists use therapeutic applications of radiation to manage cancer and other diseases. They determine the type of radiation that will be used, as well as the amount or dose, and the number and length of treatments.</p>
        <p>You may have a need for all four of these types of physicians at one time. It is beneficial to you to keep files or a journal with names and dates and copies of your medical records and procedures as your journey to wellness can be confusing and the details easy to lose.</p>
      </div>
      <div class="col">
        <h4 class="col-head">Patient Rights</h4>
        <p>Second opinions are a way to learn about your diagnosis and choices for treatment options. Some doctors are more conservative while others tend to be more aggressive. A patient has rights and one of your most important rights is the ability to get a second opinion about your diagnosis. Being informed is critical in deciding your choice of treatment.</p>
      </div>
      <div class="col">
        <p>Studies show that almost one tenth of newly diagnosed patients rarely, or never understand their diagnosis. A second opinion means you are consulting with another doctor to confirm a diagnosis and/or find possible different treatment choices available to you. It is recommended to get a second opinion immediately to avoid delays in your treatment and recovery. Seven states require insurers to cover it.</p>
      </div>
    </div>
  </div>
  <div class="page on-blue">
    <svg class="shape" viewBox="0 0 560 320" aria-hidden="true">
      <polygon points="0,130 300,0 560,0 560,320 0,320" fill="var(--blue)"/>
    </svg>
    <div class="photo" role="img" aria-label="Photo of an older couple reviewing papers together" style="left:0;top:0;width:300px;height:130px;clip-path:polygon(0 0,100% 0,0 100%)"></div>
    <p class="quote quote--white" style="left:200px;top:48px;width:340px">“A patient has rights and one of your most important rights is the ability to get a second opinion about your diagnosis. Being informed is critical in deciding your choice of treatment.”</p>
    <h4 class="col-head" style="position:absolute;left:30px;top:160px">What will it cost me?</h4>
    <div class="cols" style="left:30px;top:174px;gap:14px">
      <div class="col" style="width:114px">Assuming it is medically necessary, most insurance plans will pay for at least part of the cost while Federal Care will pay 80% of the cost of a second opinion. As a matter of fact if the second opinion doesn't agree with the first, Federal Care will pay 80% of the cost of a third opinion. Patients that belong to managed care plans may need a referral.</div>
      <div class="col" style="width:114px">Your plan may require a referral from your primary care physician, and like most HMO treatments, you must see an in-network physician. To learn about second opinions call 1-800-555-0142 or for specific rules by state for a second opinion you can visit www.fedcareplan.org.</div>
      <div class="col" style="width:114px">Review your policy before any treatment or second opinion to prevent any confusion or denial of the bill. You need to know exactly what will be covered, such as out of network provider, any lab work or testing that may be required and what your responsibilities are before seeking the second opinion.</div>
      <div class="col" style="width:114px">Ask whether tests that were completed for the initial diagnosis can be shared. You have the right to have copies of the tests you already had done. Be an informed consumer and arrive for the second opinion with all of your previous medical records, contact information, insurance card, list of prescribed medications and allergies, and any diagnostic test results.</div>
    </div>
  </div>
</section>

<!-- Inside spread: introduction and second opinions -->
<section class="spread spread--intro">
  <div class="page">
    <div class="photo" role="img" aria-label="Photo of a smiling caregiver with an older man" style="left:0;top:0;width:300px;height:200px"></div>
    <svg class="shape" viewBox="0 0 560 320" aria-hidden="true">
      <polygon points="150,60 300,60 300,320 270,320" fill="#f1f1f1"/>
      <polygon points="300,0 300,320 200,320 300,0" fill="#fff"/>
      <polygon points="0,60 150,60 270,320 0,320" fill="var(--blue)"/>
    </svg>
    <h2 class="title-big" style="left:22px;top:96px">A Clearer<br>Path</h2>
    <div class="mission" style="left:22px;top:156px;width:190px">
      <h3>Careway Kinfolk Foundation</h3>
      <h3 style="color:#fff;margin-bottom:4px">Mission Statement</h3>
      <p>Careway Kinfolk Foundation is a national non-profit organization that serves as an active liaison between the patient and their insurer, employer and/or creditors to resolve insurance, job retention and/or debt crisis matters relative to their diagnosis through case managers, doctors and attorneys. Careway Kinfolk Foundation seeks to safeguard patients through effective mediation assuring access to care, maintenance of employment and preservation of their financial stability.</p>
    </div>
    <h4 class="col-head" style="position:absolute;left:300px;top:62px;width:240px">Facts and Circumstances Relating to the Individual</h4>
    <div class="cols" style="left:300px;top:76px;gap:12px">
      <div class="col" style="width:112px">The purpose of this brochure is to address questions surrounding Second Opinions: Knowing Your Rights and Options. Making decisions about healthcare is one of the most important in a person's life. Many people are told that they have cancer or another life threatening illness and feel that they must make a decision and begin treatment as soon as possible. While this may be true in some instances,</div>
      <div class="col" style="width:112px">taking the time to learn about your disease, getting a second opinion or perhaps even a third opinion and weighing your options is a very reasonable approach. Proactive decision making will give you a greater degree of control over your treatment. Decisions regarding your health should be made after you have been thoroughly informed about your diagnosis, prognosis and available treatment options.</div>
    </div>
  </div>
  <div class="page">
    <p class="quote quote--blue" style="left:28px;top:40px;width:260px">“Proactive decision making will give you a greater degree of control over your treatment.”</p>
    <div class="cols" style="left:28px;top:100px;gap:10px">
      <div class="col" style="width:80px"><h4 class="col-head">Will my Doctor be upset if I get a second opinion?</h4>Most doctors will welcome another physician's input. Your doctor may be able to recommend a specialist. A good doctor understands your right to be well informed and should support a second opinion. You will want to obtain a copy of your medical records and test results, to share with the new doctor that you see for the second opinion.</div>
      <div class="col" style="width:80px"><h4 class="col-head">Doctor's opinions may differ</h4>A different doctor may come up with a different diagnosis, or at least offer a different opinion as to treatment choices. Not every doctor will have the same opinion with regard to diseases and possible treatments. Factors which may have an effect on a doctor's opinion are technology available to that doctor, school of thought, where they were trained, individual methods of treatment and experience.</div>
      <div class="col" style="width:80px"><h4 class="col-head">Treatment methods may differ</h4>Some doctors prefer to monitor the situation and use less aggressive procedures before moving to surgical intervention. Some doctors like to use more aggressive treatment methods from the beginning. By getting a second opinion, you can expand your options about different treatment methods which may be most suitable for you and your situation. Being informed is key.</div>
    </div>
    <h4 class="col-head" style="position:absolute;left:300px;top:38px;width:240px">Second opinions don't hurt and in fact may even help</h4>
    <div class="cols" style="left:300px;top:62px;gap:12px">
      <div class="col" style="width:112px">It never hurts to get a second opinion. Keep in mind that doctors are human and they too can make mistakes or be faced with unusual or challenging cases. When the first doctor's opinion is the same or similar to the second doctor's, your confidence will be increased. There is nothing lost by visiting one more doctor just to make sure that the first doctor's opinion is correct. With serious illnesses that may require extended treatment, you should feel confident that you have chosen the most appropriate treatment for your particular situation. A valid opinion and</div>
      <div class="col" style="width:112px">appropriate course of treatment is your best option for return to good health or grasping control of the chronic disease. While second opinions may be awkward for doctor and patient at times, studies have shown that 30 percent of patients, who sought second opinions for elective surgery and 18 percent of those who were required to obtain a second opinion by their insurance company, found that the two opinions were not in agreement. These studies are one more reason why you need to make sure you are educated properly to make the best decision for your health.</div>
    </div>
  </div>
</section>

<!-- Front cover -->
<section class="cover cover--front">
  <div class="photo" role="img" aria-label="Black and white portrait photo of an older couple" style="inset:0;clip-path:polygon(0 0,70% 0,100% 0,100% 21%,6% 100%,0 100%)"></div>
  <svg class="shape" viewBox="0 0 540 290" aria-hidden="true">
    <polygon points="380,0 540,0 540,62" fill="var(--blue)"/>
    <polygon points="0,290 0,250 40,290" fill="var(--blue)"/>
  </svg>
  <div class="brand"><span class="brand-dot"></span>Careway Kinfolk Foundation</div>
  <p class="series">A CLEARER PATH</p>
  <h1 class="cover-title">Second Opinions: Know Your<br>Rights and Options</h1>
</section>

<!-- Back cover -->
<section class="cover cover--back">
  <svg class="shape" viewBox="0 0 540 290" aria-hidden="true">
    <polygon points="0,200 90,290 0,290" fill="var(--blue)"/>
  </svg>
  <p class="back-intro">Careway Kinfolk Foundation is dedicated to ensuring that all Americans have access to care and resources available to assist patients affected by debilitating or life threatening illness, helping them to be able to make informed decisions about their health. For further information, either call the Foundation or view the publications below.</p>
  <div class="pubs">
    <ul>
      <li>Steps Through a Disability Claim<span>Available in English &amp; Spanish</span></li>
      <li>Finding Financial Help: A Regional Listing of Aid Programs</li>
      <li>Caring Ahead: Money Basics for Families of Young Patients</li>
      <li>Saving on Everyday Care</li>
      <li>Small Steps to Better Health</li>
    </ul>
    <ul>
      <li>Healthy Neighbors: Community Wellness Notes</li>
      <li>Healthy Roots: Family Wellness Notes</li>
      <li>“A Clearer Path” series<span>A set of short pamphlets written to answer the questions patients ask most often about health care.</span></li>
    </ul>
  </div>
  <div class="contact">
    <p>421 Harbor Way, Suite 200<br>Bayview, VA 23000</p>
    <p>E: <span class="hl">help@carewaykinfolk.org</span><br><span class="hl">www.carewaykinfolk.org</span></p>
  </div>
</section>

</body>
</html>
```